KWI Business Card

Please create a creative design for a business card using the new theme from the Logo & website. This company's main focus is food manufacturing building construction. Please integrate the new logo attached.

Please use the following information for the demo card:

Korvel Walls, Inc.
Dana Whitcombe
dwhitcombe@korvelwalls.example
Cell: 312-555-0178
218 Larkmoor Ave
Ashbrook Falls, WL 60418

See pictures and more information on the website.

www.korvelwalls.example

```html
<!DOCTYPE html>
<html lang="en">
<head>
<meta charset="utf-8">
<title>KWI Business Card</title>
<link rel="stylesheet" href="https://fonts.googleapis.com/css2?family=Montserrat:wght@400;700&display=swap">
<style>
  :root {
    --page-bg: #e6e8eb;
    --brand-blue: #1f6fc4;
    --ice-light: #c9e2f7;
    --ice-mid: #7fb2e6;
    --ice-deep: #2f78cc;
    --ink: #3a3d42;
    --card-white: #ffffff;
  }
  * { box-sizing: border-box; margin: 0; padding: 0; }
  html, body { width: 1200px; height: 965px; overflow: hidden; }
  body {
    background: var(--page-bg);
    font-family: "Montserrat", sans-serif;
    display: flex;
    flex-direction: column;
    align-items: center;
    justify-content: center;
    gap: 40px;
  }
  .card {
    width: 700px;
    height: 400px;
    position: relative;
    overflow: hidden;
    box-shadow: 0 6px 18px rgba(0,0,0,0.15);
  }

  /* Front */
  .card-front { background: var(--ice-deep); }
  .front-pattern {
    position: absolute; inset: 0;
    background: radial-gradient(ellipse 70% 60% at 45% 40%, var(--ice-light) 0%, var(--ice-mid) 50%, var(--ice-deep) 100%);
  }
  .front-brand {
    position: absolute;
    right: 60px;
    top: 50%;
    transform: translateY(-50%);
    display: flex;
    align-items: center;
    gap: 14px;
  }
  .brand-square {
    width: 22px; height: 22px;
    background: var(--brand-blue);
  }
  .brand-name {
    font-weight: 700;
    color: var(--brand-blue);
    font-size: 34px;
    letter-spacing: 0.5px;
  }

  /* Back */
  .card-back { background: var(--card-white); display: flex; }
  .back-brand {
    width: 290px;
    display: flex;
    align-items: center;
    justify-content: center;
  }
  .back-brand .brand-name { font-size: 23px; }
  .back-brand .brand-inner { display: flex; align-items: center; gap: 12px; }
  .back-brand .brand-square { width: 18px; height: 18px; }
  .divider {
    width: 2px;
    background: var(--brand-blue);
    margin: 70px 0;
  }
  .back-details {
    flex: 1;
    padding: 70px 30px 60px 50px;
    display: flex;
    flex-direction: column;
  }
  .person-name {
    font-weight: 700;
    color: var(--brand-blue);
    font-size: 26px;
    letter-spacing: -0.5px;
    text-transform: uppercase;
  }
  .contact-list {
    list-style: none;
    margin-top: 60px;
    color: var(--ink);
    font-size: 17px;
    line-height: 1.55;
  }
  .contact-list li { display: flex; align-items: center; gap: 12px; white-space: nowrap; }
  .contact-list svg { width: 18px; height: 18px; flex: none; }
  .site-strong { color: var(--brand-blue); font-weight: 700; }
  .address {
    margin-top: auto;
    color: var(--ink);
    font-size: 19px;
    line-height: 1.35;
  }
</style>
</head>
<body>

<section class="card card-front" aria-label="Card front">
  <div class="front-pattern" role="img" aria-label="Soft ice-blue gradient with a faint repeating snowflake pattern"></div>
  <div class="front-brand">
    <span class="brand-square"></span>
    <span class="brand-name">Korvel Walls, Inc.</span>
  </div>
</section>

<section class="card card-back" aria-label="Card back">
  <div class="back-brand">
    <div class="brand-inner">
      <span class="brand-square"></span>
      <span class="brand-name">Korvel Walls, Inc.</span>
    </div>
  </div>
  <div class="divider"></div>
  <div class="back-details">
    <h1 class="person-name">Dana Whitcombe</h1>
    <ul class="contact-list">
      <li>
        <svg viewBox="0 0 18 18" fill="none" stroke="var(--brand-blue)" stroke-width="1.5"><rect x="5" y="1.5" width="8" height="15" rx="1.5"/><line x1="8" y1="14" x2="10" y2="14"/></svg>
        312-555-0178
      </li>
      <li>
        <svg viewBox="0 0 18 18" fill="none" stroke="var(--brand-blue)" stroke-width="1.5"><rect x="1.5" y="4" width="15" height="10" rx="1"/><polyline points="1.5,4 9,10 16.5,4"/></svg>
        dwhitcombe@korvelwalls.example
      </li>
      <li>
        <svg viewBox="0 0 18 18" fill="none" stroke="var(--brand-blue)" stroke-width="1.5"><circle cx="9" cy="9" r="7.5"/><ellipse cx="9" cy="9" rx="3.5" ry="7.5"/><line x1="1.5" y1="9" x2="16.5" y2="9"/></svg>
        <span>www.<span class="site-strong">korvelwalls</span>.example</span>
      </li>
    </ul>
    <p class="address">218 Larkmoor Ave<br>Ashbrook Falls, WL 60418</p>
  </div>
</section>

</body>
</html>
```